Cat-products company needs smart, yet endearing, business card

We need a business card design for a new, but up-and-running, business based in Honolulu, Hawaii. The business is Purrlane Nest Co. Our first product is the most environmentally-friendly cat grass kit ever seen on the planet. Future products, currently in the R&D phase, will include a variety of exciting cat scratchers. We also do consulting work to help apartment-dwellers make their home more cat-friendly and, in the future, plan on doing full, custom installs of structure to create high walkways for cats.

Target Market(s)

Middle-aged, apartment-dwelling, middle-class workers who own 1 or more cats and who dote on them.

Industry/Entity Type

Pet Care

Contact Information for Business Card

A striking, professional, yet warm and friendly design is what we're after.

Font styles to use
Serif
Sans Serif
Other font styles liked:
• Comfortaa

Colors

Designer to choose colors to be used in the design.

Requirements
Must have
• The company logo: (see attachment)
• The company name: Purrlane Nest Co
• The web address: www.purrlanenestco.example
• Email: support@purrlanenestco.example
• Phone: +1 (808) 574 1630
• Update (Fri Jun 30 3017 7:45pm Hawaii Time) I would like, is possible, uploaded picture of the cat grass kit on the back of the card with some text along the lines of: Purrlane Nest Co - Maker Of The Freshest Cat Grass Kit Yet
Nice to have
• A cat picture, cartoon, real or silhouette that illustrates cats in action and/or relaxing; ie using the apartment space to live, play and relax in and being well-contented.
• Most of the website is done in the font: Comfortaa. It might be nice to continue using this for brand consistency.
Should not have
• Hard-to-read fonts.

```html
<!DOCTYPE html>
<html lang="en">
<head>
<meta charset="utf-8">
<title>Purrlane Nest Co — Business Card</title>
<link href="https://fonts.googleapis.com/css2?family=Comfortaa:wght@400;700&display=swap" rel="stylesheet">
<style>
  :root {
    --backdrop: #3b3b3d;
    --card: #ffffff;
    --amber: #f4b01b;
    --cocoa: #5a3a2e;
    --ink: #2e2a28;
    --rule: #6a6462;
  }
  * { box-sizing: border-box; margin: 0; padding: 0; }
  html, body {
    width: 1200px; height: 1000px; overflow: hidden;
    background: var(--backdrop);
    font-family: "Comfortaa", sans-serif;
  }
  .stage {
    position: relative; width: 1200px; height: 1000px;
  }
  .card {
    position: absolute; left: 215px; width: 770px; height: 440px;
    background: var(--card);
    box-shadow: 0 12px 30px rgba(0,0,0,0.45);
    overflow: hidden;
  }
  .card--front { top: 40px; }
  .card--back { top: 520px; }

  .brand {
    display: flex; align-items: center; gap: 14px;
  }
  .brand__mark {
    width: 46px; height: 46px; background: var(--cocoa); border-radius: 6px;
  }
  .brand__name {
    font-weight: 700; color: var(--amber); font-size: 34px; line-height: 1;
  }
  .card--front .brand {
    position: absolute; left: 50%; top: 50%; transform: translate(-50%, -50%);
  }

  .card--back .brand { position: absolute; left: 44px; top: 48px; }
  .card--back .brand__name { font-size: 28px; }

  .holder {
    position: absolute; right: 50px; top: 44px; text-align: right;
  }
  .holder__name {
    font-size: 30px; font-weight: 700; color: var(--amber); letter-spacing: 0.5px;
  }
  .holder__role {
    font-size: 16px; color: var(--ink); margin-top: 4px;
  }
  .holder-rule {
    position: absolute; left: 44px; top: 128px; width: 560px; height: 1.5px;
    background: var(--rule);
  }

  .contacts {
    position: absolute; right: 50px; top: 150px; list-style: none; text-align: right;
  }
  .contacts li {
    display: flex; justify-content: flex-end; align-items: center; gap: 12px;
    font-size: 17px; color: var(--ink); line-height: 30px;
  }
  .contacts svg { width: 16px; height: 16px; fill: var(--amber); flex: none; }
  .contacts .accent { color: var(--amber); }

  .address {
    position: absolute; left: 50px; top: 292px;
    font-size: 18px; color: var(--ink); line-height: 28px;
  }
  .swoosh { position: absolute; left: 0; bottom: 0; width: 770px; height: 440px; }
</style>
</head>
<body>
<main class="stage">
  <section class="card card--front" aria-label="Card front">
    <div class="brand">
      <span class="brand__mark"></span>
      <span class="brand__name">Purrlane Nest Co</span>
    </div>
  </section>

  <section class="card card--back" aria-label="Card back">
    <svg class="swoosh" viewBox="0 0 770 440" aria-hidden="true">
      <path d="M0 428 L0 420 L470 398 C545 394 575 360 610 346 L614 352 C580 366 548 402 472 406 Z" fill="var(--amber)"/>
      <path d="M0 440 L0 432 L480 412 C575 406 600 352 690 338 L770 332 L770 440 Z" fill="var(--cocoa)"/>
    </svg>

    <div class="brand">
      <span class="brand__mark"></span>
      <span class="brand__name">Purrlane Nest Co</span>
    </div>

    <div class="holder">
      <p class="holder__name">Noelani Park</p>
      <p class="holder__role">Director</p>
    </div>
    <div class="holder-rule"></div>

    <ul class="contacts">
      <li>+1 (808) 574 1630
        <svg viewBox="0 0 16 16"><path d="M4 1l3 3-2 2c1 2 3 4 5 5l2-2 3 3-2 3C7 15 1 9 1 3z"/></svg></li>
      <li>support@purrlanenestco.example
        <svg viewBox="0 0 16 16"><path d="M1 3h14v10H1z M1 3l7 6 7-6" stroke="#fff" stroke-width="1"/></svg></li>
      <li><span>www.<span class="accent">purrlanenestco</span>.example</span>
        <svg viewBox="0 0 16 16"><circle cx="8" cy="8" r="7"/><path d="M1 8h14M8 1c-3 4-3 10 0 14M8 1c3 4 3 10 0 14" stroke="#fff" stroke-width="1" fill="none"/></svg></li>
    </ul>

    <p class="address">Your Street Address,<br>Country,1234</p>
  </section>
</main>
</body>
</html>
```